Asia Hotel need a card and logo

The new hotel in East Asia, Taiwan need a business card and logo design.The hotel's Chinese name is 岚柏文旅,English name is "Velmira Hotel".The core concept of this hotel is "Eco green", going to use many plant etc.,The building's first outlook draft is attached in the file for your reference.The style be modern and fashion will be good. Thank you.
Target Market(s)
East Asia
Industry/Entity Type
Hotel
Contact Information for Business Card
The hotel's name both in Chinese and English :岚柏商旅 Velmira Hotel
The logo, address, E-mail and tel number place.
Stuff's name and title.
Font styles to use
Colors
Designer to choose colors to be used in the design.
Look and feel
Each slider illustrates characteristics of the customer's brand and the style your logo design should communicate.

```html
<!DOCTYPE html>
<html lang="zh-Hant">
<head>
<meta charset="utf-8">
<title>岚柏商旅 · Velmira Hotel — Business Card</title>
<link rel="stylesheet" href="https://fonts.googleapis.com/css2?family=Noto+Sans+SC:wght@300&family=Open+Sans:wght@400&family=Saira:wght@300&display=swap">
<style>
  :root {
    --bg-center: #6b6c6c;
    --bg-edge: #2e2e2e;
    --card-black: #181818;
    --card-white: #ffffff;
    --gold: #f2a71b;
    --icon-grey: #e2e2e2;
    --ink: #1a1a1a;
  }
  html, body {
    margin: 0;
    padding: 0;
    width: 1200px;
    height: 1200px;
    overflow: hidden;
  }
  .canvas {
    position: relative;
    width: 1200px;
    height: 1200px;
    background: radial-gradient(ellipse at 50% 50%, var(--bg-center) 0%, #555656 45%, var(--bg-edge) 100%);
  }
  .card {
    position: absolute;
    top: 183px;
    width: 480px;
    height: 840px;
    background: var(--card-black);
    overflow: hidden;
  }
  .card--front { left: 112px; }
  .card--back { left: 623px; }

  .front-wave {
    position: absolute;
    inset: 0;
    width: 480px;
    height: 840px;
  }
  .front-name-cn {
    position: absolute;
    left: 118px;
    top: 34px;
    writing-mode: vertical-rl;
    font-family: "Noto Sans SC", sans-serif;
    font-weight: 300;
    font-size: 54px;
    line-height: 1;
    letter-spacing: 1px;
    color: var(--ink);
    margin: 0;
  }

  .brand-lockup {
    position: absolute;
    display: flex;
    flex-direction: column;
    align-items: center;
    gap: 10px;
    transform: translate(-50%, -50%);
  }
  .brand-lockup__dot {
    width: 14px;
    height: 14px;
    border: 2px solid var(--gold);
    border-radius: 50%;
  }
  .brand-lockup__name {
    font-family: "Open Sans", sans-serif;
    font-weight: 400;
    font-size: 19px;
    letter-spacing: 0.5px;
    color: var(--gold);
    white-space: nowrap;
  }
  .brand-lockup--front { left: 168px; top: 726px; }
  .brand-lockup--back { left: 241px; top: 209px; }

  .contact-list {
    position: absolute;
    left: 0;
    top: 0;
    margin: 0;
    padding: 0;
    list-style: none;
  }
  .contact-item {
    position: absolute;
    left: 0;
    width: 460px;
  }
  .contact-item__icon {
    position: absolute;
    left: 116px;
    width: 40px;
    height: 40px;
    transform: translateY(-50%);
  }
  .contact-item__text {
    position: absolute;
    left: 184px;
    font-family: "Open Sans", sans-serif;
    font-size: 15px;
    color: var(--gold);
    white-space: nowrap;
    transform: translateY(-50%);
    line-height: 1.25;
  }
  .contact-item__text--address {
    left: 180px;
    font-family: "Saira", sans-serif;
    font-weight: 300;
    font-size: 16.5px;
    letter-spacing: 0.4px;
  }
  .contact-item--address { top: 562px; }
  .contact-item--email { top: 622px; }
  .contact-item--phone { top: 682px; }
  .contact-item--web { top: 742px; }
</style>
</head>
<body>
<main class="canvas">

  <section class="card card--front" aria-label="Card front">
    <svg class="front-wave" viewBox="0 0 600 1050" preserveAspectRatio="none" aria-hidden="true">
      <path fill="#ffffff" d="M85 0 H600 V1050 H433 C432 950 431 870 405 790 C375 700 330 660 250 580 C170 500 120 450 102 370 C90 330 85 300 85 280 Z"/>
    </svg>
    <h1 class="front-name-cn">岚柏商旅</h1>
    <div class="brand-lockup brand-lockup--front">
      <span class="brand-lockup__dot"></span>
      <span class="brand-lockup__name">VELMIRA HOTEL</span>
    </div>
  </section>

  <section class="card card--back" aria-label="Card back">
    <div class="brand-lockup brand-lockup--back">
      <span class="brand-lockup__dot"></span>
      <span class="brand-lockup__name">VELMIRA HOTEL</span>
    </div>

    <ul class="contact-list">
      <li class="contact-item contact-item--address">
        <svg class="contact-item__icon" viewBox="0 0 40 40" aria-hidden="true">
          <path fill="var(--icon-grey)" d="M20 4 C13 4 9 9 9 15 C9 23 20 36 20 36 C20 36 31 23 31 15 C31 9 27 4 20 4 Z"/>
          <circle cx="20" cy="15" r="4.5" fill="var(--card-black)"/>
        </svg>
        <span class="contact-item__text contact-item__text--address">Lanbo Road, Da'an Dist,<br>Number 12/A, 10617</span>
      </li>
      <li class="contact-item contact-item--email">
        <svg class="contact-item__icon" viewBox="0 0 40 40" aria-hidden="true">
          <rect x="4" y="8" width="34" height="24" fill="none" stroke="var(--icon-grey)" stroke-width="2.2"/>
          <path d="M4 8 L21 22 L38 8 M4 32 L16 18 M38 32 L26 18" fill="none" stroke="var(--icon-grey)" stroke-width="2.2"/>
        </svg>
        <span class="contact-item__text">info@velmirahotel.com</span>
      </li>
      <li class="contact-item contact-item--phone">
        <svg class="contact-item__icon" viewBox="0 0 40 40" aria-hidden="true">
          <path fill="var(--icon-grey)" d="M8 5 L14 4 L18 13 L14 17 C16 22 19 25 24 27 L28 23 L37 27 L36 33 C35 36 32 37 29 36 C17 33 8 24 5 12 C4 9 5 6 8 5 Z"/>
        </svg>
        <span class="contact-item__text">+886 2 5550 1847</span>
      </li>
      <li class="contact-item contact-item--web">
        <svg class="contact-item__icon" viewBox="0 0 40 40" aria-hidden="true">
          <g fill="none" stroke="var(--icon-grey)" stroke-width="3" stroke-linecap="round">
            <path d="M4 15 C14 5 28 5 38 15"/>
            <path d="M9 20 C16 13 26 13 33 20"/>
            <path d="M14 25 C18 21 24 21 28 25"/>
          </g>
          <circle cx="21" cy="31" r="3" fill="var(--icon-grey)"/>
        </svg>
        <span class="contact-item__text">www.velmirahotel.com</span>
      </li>
    </ul>
  </section>

</main>
</body>
</html>
```